Shopping Cart needed

I've designed 95% of my website with Wix. I need some help creating a shopping cart and linking it to my tendrix business account. I'm in the services business. They're only buying virtual services that my company provides.
In my mind, I'd like for the customer to click a button and be taken to a page that lists out the options for them to purchase. There could be up to three things that they'd like to buy, using radio buttons. Have it then take those expenses, total them and launch Tendrix for them to complete the checkout.
Two of my five products are recurring monthly charges. Integrating that into it is important. They'll only select one of these type of charges.
Any help would be greatly appreciated. It's all I need between now and launching the site. Thanks!

```html
<!DOCTYPE html>
<html lang="en">
<head>
<meta charset="utf-8">
<title>Order Information Form</title>
<link href="https://fonts.googleapis.com/css2?family=Open+Sans:wght@400;600;700&family=Arimo:wght@400;700&display=swap" rel="stylesheet">
<style>
:root{
  --brand-red:#c8100f;
  --ink:#111;
  --body:#222;
  --line:#888;
  --button:#cc0f0f;
  --button-edge:#8a8a8a;
  --card-blue:#1d3f7a;
  --paper:#fff;
}
*{box-sizing:border-box;margin:0;padding:0}
html,body{width:974px;height:1200px;overflow:hidden;background:var(--paper)}
body{position:relative;font-family:"Open Sans",Arial,sans-serif;color:var(--ink)}
.abs{position:absolute}
.form-title{left:30px;top:29px;font-size:27px;font-weight:700;color:var(--brand-red);line-height:36px}
.form-intro{left:30px;top:85px;font-size:18.2px;line-height:24px;color:var(--ink)}
.service{left:30px;width:900px}
.service-head{display:flex;align-items:center;height:22px}
.checkbox{width:13px;height:13px;border:1px solid var(--line);background:#f4f4f4;margin-right:6px;display:inline-block;position:relative}
.checkbox svg{position:absolute;left:0;top:0}
.service-name{font-size:18px;font-weight:700;color:var(--brand-red)}
.service-body{margin-left:19px;width:400px;font-size:13px;line-height:20px;color:var(--body)}
.service-body ul{list-style:none}
.service-body li{position:relative;padding-left:22px}
.service-body li::before{content:"";position:absolute;left:8px;top:8px;width:5px;height:5px;border-radius:50%;background:var(--ink)}
.price{position:absolute;left:419px;font-size:16px;font-weight:700;line-height:22px;color:var(--ink);width:210px}
.radio-row{display:flex;align-items:center;margin-left:5px}
.radio{width:11px;height:11px;border-radius:50%;border:1px solid var(--line);background:#eee;margin-right:8px;position:relative}
.radio.on::after{content:"";position:absolute;left:2px;top:2px;width:5px;height:5px;border-radius:50%;background:#2a3e5a}
.summary-title{left:30px;top:926px;font-size:18px;font-weight:700;color:var(--brand-red)}
.summary-row{left:30px;font-size:16px;line-height:22px;color:var(--ink)}
.summary-row .amount{position:absolute;white-space:nowrap}
.after-note{left:30px;top:1064px;font-size:12px;color:var(--ink)}
.order-button{left:30px;top:1093px;width:274px;height:33px;background:var(--button);border:1px solid var(--button-edge);color:#fff;font-family:Arimo,Arial,sans-serif;font-size:13px;display:flex;align-items:center;justify-content:center}
.payment-methods{left:70px;top:1132px;display:flex;gap:2px}
.method{width:33px;height:20px;border:1px solid #b9b9b9;background:#fafafa;font-family:Arimo,Arial,sans-serif;font-size:7px;font-weight:700;color:var(--card-blue);display:flex;align-items:center;justify-content:center}
.payment-note{left:72px;top:1156px;font-family:Arimo,Arial,sans-serif;font-size:10.5px;font-weight:700;color:var(--card-blue)}
</style>
</head>
<body>
<h1 class="abs form-title">Order Information Form</h1>
<p class="abs form-intro">Choose which services you would like Brightpath Social to provide for you:</p>

<section class="abs service" style="top:129px">
  <div class="service-head"><span class="checkbox"></span><h2 class="service-name">Profile Creation</h2></div>
  <div class="service-body">
    <p>Chirpline account set up and support. Includes:</p>
    <ul>
      <li>Set up a Chirpline profile</li>
      <li>A unique Chirpline "handle"</li>
      <li>A personalized display image</li>
      <li>A customized profile banner &amp; bio</li>
    </ul>
    <p>Once you're set up, we'll help you get plugged in on your laptop, smart phone or other wireless device through our recommended list of apps.</p>
  </div>
  <p class="price" style="top:23px">One-time fee of $99</p>
</section>

<section class="abs service" style="top:337px">
  <div class="service-head"><span class="checkbox"></span><h2 class="service-name">Content Creation</h2></div>
  <div class="service-body">
    <p>Our social media strategists will scour the internet to provide the content to post each day, including favorite websites, news bureaus, hobbies, interests and professional outlets.<br>5-10 items posted per day with localized hashtags.</p>
  </div>
  <div class="price" style="top:23px">
    <p>One-time fee of $49 +</p>
    <p class="radio-row"><span class="radio on"></span>$99 per month</p>
    <p class="radio-row"><span class="radio"></span>$999 per year</p>
  </div>
</section>

<section class="abs service" style="top:465px">
  <div class="service-head"><span class="checkbox"><svg width="11" height="11" viewBox="0 0 11 11"><path d="M2 5.5l2.3 2.3L9 2.8" fill="none" stroke="#333" stroke-width="1.6"/></svg></span><h2 class="service-name">Strategy Analysis</h2></div>
  <div class="service-body">
    <p>Analize existing Chirpline following for potential customers. Develop various strategies for certain industries. This includes monthly analytic reports about your posts, views, followers and other demographic data. It also includes a strategic summary of our recommendations for your social media strategy.</p>
  </div>
  <p class="price" style="top:23px">$299 per analysis report, or<br>$99 per report with Profile Management service</p>
</section>

<section class="abs service" style="top:623px">
  <div class="service-head"><span class="checkbox"><svg width="11" height="11" viewBox="0 0 11 11"><path d="M2 5.5l2.3 2.3L9 2.8" fill="none" stroke="#333" stroke-width="1.6"/></svg></span><h2 class="service-name">Profile Management</h2></div>
  <div class="service-body">
    <p>Brightpath Social will completely manage your Chirpline profile. This is the "full service" version which includes:</p>
    <ul>
      <li>Profile Creation service</li>
      <li>Content Creation service</li>
      <li>Strategic Analysis reports for $99 per report</li>
      <li>Re-chirping content from your followers</li>
      <li>Engaging followers over the direct message space</li>
      <li>Responding to all inquiries to your Chirpline account</li>
      <li>Favoriting chirps from your followers</li>
      <li>Following people on your behalf each week to build your following</li>
      <li>Essentially, it's us working for you without us being on your payroll!</li>
    </ul>
  </div>
  <p class="price" style="top:23px">$999 per month</p>
</section>

<h2 class="abs summary-title">Purchase Summary:</h2>
<div class="abs summary-row" style="top:965px">Profile Management service<span class="amount" style="left:230px;top:0">$999 per year</span></div>
<div class="abs summary-row" style="top:987px">Strategic Analysis report<span class="amount" style="left:239px;top:0">$99</span></div>
<div class="abs summary-row" style="top:1031px">Total Due:<span class="amount" style="left:221px;top:0">$1098</span></div>
<p class="abs after-note">After placing your order, you will be directed to your account management page.</p>

<div class="abs order-button">Place your order</div>
<div class="abs payment-methods">
  <span class="method">Varda</span>
  <span class="method">Meridian</span>
  <span class="method">Amberline</span>
  <span class="method">Dovecard</span>
  <span class="method">Tendrix</span>
</div>
<p class="abs payment-note">NO TENDRIX ACCOUNT NEEDED!</p>
</body>
</html>
```